International wholesale business needs a business card

We need a business card.

Company Details:
Company Name and logo
Address, Phone number, Website
Employee Details:
Name, Designation, Mobile Number & Email address

Logo file is attached.

```html
<!DOCTYPE html>
<html lang="en">
<head>
<meta charset="utf-8">
<title>Corvane Trading – Business Card</title>
<link href="https://fonts.googleapis.com/css2?family=Montserrat:wght@400;600;700&display=swap" rel="stylesheet">
<style>
  :root {
    --brand-red: #c4262e;
    --swoosh-grey: #eef0f0;
    --text-grey: #8a8f94;
    --card-white: #ffffff;
    --page-bg: #e4e5e7;
  }
  html, body {
    margin: 0;
    width: 1200px;
    height: 1024px;
    overflow: hidden;
    background: var(--page-bg);
    font-family: "Montserrat", sans-serif;
  }
  .sheet {
    position: relative;
    width: 1200px;
    height: 1024px;
  }
  .card {
    position: absolute;
    left: 300px;
    width: 600px;
    height: 343px;
    background: var(--card-white);
    overflow: hidden;
    box-shadow: 0 6px 20px rgba(0,0,0,0.18);
  }
  .card--front { top: 150px; }
  .card--back { top: 533px; }
  .card__art {
    position: absolute;
    inset: 0;
    width: 100%;
    height: 100%;
  }
  .swoosh { fill: var(--swoosh-grey); }
  .panel-red { fill: var(--brand-red); }
  .panel-white { fill: var(--card-white); }

  .wordmark {
    position: absolute;
    display: flex;
    align-items: center;
    gap: 12px;
    color: var(--brand-red);
    font-weight: 700;
    letter-spacing: 1px;
  }
  .wordmark__dot {
    width: 30px;
    height: 30px;
    border-radius: 50%;
    background: var(--brand-red);
  }
  .card--front .wordmark {
    left: 36px;
    top: 46px;
    font-size: 30px;
    line-height: 1;
  }
  .company-details {
    position: absolute;
    left: 40px;
    bottom: 46px;
    color: var(--text-grey);
    font-size: 13px;
    line-height: 1.5;
  }
  .company-details__name {
    color: var(--brand-red);
    font-weight: 700;
    font-size: 16px;
    letter-spacing: 0.5px;
    margin-bottom: 4px;
  }
  .detail-row {
    display: flex;
    align-items: center;
    gap: 7px;
  }
  .detail-row svg { width: 11px; height: 11px; flex: none; }
  .detail-row--plain { padding-left: 18px; }

  .employee {
    position: absolute;
    left: 378px;
    top: 128px;
    color: #fff;
    font-size: 13px;
    line-height: 1.5;
  }
  .employee__name {
    font-weight: 700;
    font-size: 16px;
    letter-spacing: 0.5px;
  }
  .employee__role {
    font-size: 11px;
    margin-bottom: 4px;
  }
  .employee .detail-row svg { fill: #fff; }

  .card--back .wordmark {
    left: 0;
    right: 0;
    top: 118px;
    flex-direction: column;
    gap: 6px;
    text-align: center;
  }
  .wordmark__primary { font-size: 46px; line-height: 1; letter-spacing: 2px; }
  .wordmark__secondary { font-size: 18px; letter-spacing: 12px; line-height: 1; }
</style>
</head>
<body>
<main class="sheet">

  <section class="card card--front" aria-label="Business card front">
    <svg class="card__art" viewBox="0 0 600 343" aria-hidden="true">
      <path class="swoosh" d="M470 40 C370 58 312 130 326 212 C336 272 384 316 446 343 L470 343 C400 300 356 240 360 178 C366 108 416 62 470 40 Z"/>
      <path class="panel-red" d="M600 112 C545 56 432 46 378 104 C332 154 336 240 396 290 C420 311 440 328 462 343 L600 343 Z"/>
    </svg>

    <div class="wordmark">
      <span class="wordmark__dot"></span>
      <span>CORVANE TRADING</span>
    </div>

    <div class="company-details">
      <div class="company-details__name">CORVANE TRADING</div>
      <div class="detail-row">
        <svg viewBox="0 0 24 24" fill="#c4262e"><path d="M6.6 10.8a15.1 15.1 0 0 0 6.6 6.6l2.2-2.2a1 1 0 0 1 1-.25 11.4 11.4 0 0 0 3.6.57 1 1 0 0 1 1 1V20a1 1 0 0 1-1 1A17 17 0 0 1 3 4a1 1 0 0 1 1-1h3.5a1 1 0 0 1 1 1c0 1.25.2 2.45.57 3.57a1 1 0 0 1-.25 1z"/></svg>
        <span>555-014-2290</span>
      </div>
      <div class="detail-row">
        <svg viewBox="0 0 24 24" fill="none" stroke="#c4262e" stroke-width="2.4"><circle cx="12" cy="12" r="9.5"/><path d="M2.5 12h19M12 2.5c3 3 3 16 0 19M12 2.5c-3 3-3 16 0 19"/></svg>
        <span>www.corvanetrading.com</span>
      </div>
      <div class="detail-row detail-row--plain">4821 Harbor View Rd. Suite 210</div>
      <div class="detail-row detail-row--plain">Austin, TX 78701</div>
    </div>

    <div class="employee">
      <div class="employee__name">EMPLOYEE NAME</div>
      <div class="employee__role">Managing Member</div>
      <div class="detail-row">
        <svg viewBox="0 0 24 24"><path d="M6.6 10.8a15.1 15.1 0 0 0 6.6 6.6l2.2-2.2a1 1 0 0 1 1-.25 11.4 11.4 0 0 0 3.6.57 1 1 0 0 1 1 1V20a1 1 0 0 1-1 1A17 17 0 0 1 3 4a1 1 0 0 1 1-1h3.5a1 1 0 0 1 1 1c0 1.25.2 2.45.57 3.57a1 1 0 0 1-.25 1z"/></svg>
        <span>555-014-2290</span>
      </div>
      <div class="detail-row">
        <svg viewBox="0 0 24 24"><path d="M2 5h20v14H2z M3 6l9 7 9-7" fill="#fff" stroke="#c4262e" stroke-width="1.6"/></svg>
        <span>info@corvanetrading.com</span>
      </div>
    </div>
  </section>

  <section class="card card--back" aria-label="Business card back">
    <svg class="card__art" viewBox="0 0 600 343" aria-hidden="true">
      <ellipse class="swoosh" cx="240" cy="95" rx="345" ry="222"/>
      <ellipse class="panel-white" cx="235" cy="80" rx="315" ry="196"/>
      <path class="panel-red" d="M545 0 C640 90 610 262 420 308 C330 330 240 334 150 343 L600 343 L600 0 Z"/>
    </svg>

    <div class="wordmark">
      <span class="wordmark__primary">CORVANE</span>
      <span class="wordmark__secondary">TRADING</span>
    </div>
  </section>

</main>
</body>
</html>
```